Corporate Business Cards

We need a new design for all of our business cards. They are boring and need some life.

Industry/Entity Type

Business

Requirements
Must have
• Corporate Logo of some type (See attached Pyramid)

Corporate Phrase "Accelerating Cashflow"

```html
<!DOCTYPE html>
<html lang="en">
<head>
<meta charset="utf-8">
<title>Ledgerwise Partners – Business Card</title>
<link rel="stylesheet" href="https://fonts.googleapis.com/css2?family=Tinos:wght@700&family=Questrial&family=Mulish:wght@400;700&display=swap">
<style>
  :root {
    --backdrop: #e6e7ea;
    --card-light: #2466d6;
    --card-mid: #1547b8;
    --card-dark: #0a2784;
    --ink: #ffffff;
    --ink-soft: #dfe7f7;
    --ink-muted: rgba(223, 231, 247, 0.78);
    --band: rgba(120, 170, 255, 0.22);
    --shadow: rgba(10, 25, 70, 0.28);
  }
  * { box-sizing: border-box; margin: 0; padding: 0; }
  html, body {
    width: 1200px;
    height: 871px;
    overflow: hidden;
    background: var(--backdrop);
  }
  .canvas {
    position: relative;
    width: 1200px;
    height: 871px;
  }
  .business-card {
    position: absolute;
    left: 100px;
    top: 150px;
    width: 1000px;
    height: 571px;
    overflow: hidden;
    background:
      radial-gradient(ellipse 70% 75% at 45% 45%, var(--card-light) 0%, var(--card-mid) 55%, var(--card-dark) 100%);
    box-shadow: 0 18px 40px var(--shadow);
    color: var(--ink);
  }
  .accent-band {
    position: absolute;
    left: 0;
    top: 238px;
    width: 560px;
    height: 12px;
    background: var(--band);
  }
  .brand {
    position: absolute;
    left: 160px;
    top: 72px;
    display: flex;
    align-items: flex-start;
    gap: 36px;
  }
  .brand-mark {
    width: 40px;
    height: 40px;
    margin-top: 14px;
    background: var(--ink);
  }
  .brand-name {
    font-family: "Tinos", "Times New Roman", serif;
    font-weight: 700;
    font-size: 54px;
    line-height: 1.02;
    letter-spacing: 1px;
    text-transform: uppercase;
    color: var(--ink);
  }
  .brand-name .line { display: block; }
  .brand-name .line-indented { padding-left: 36px; }
  .holder {
    position: absolute;
    left: 90px;
    top: 272px;
    font-family: "Mulish", "Century Gothic", sans-serif;
    font-size: 27px;
    line-height: 1.2;
    color: var(--ink);
  }
  .holder-name { font-weight: 700; }
  .holder-divider { margin: 0 10px; font-weight: 400; }
  .holder-role { font-weight: 400; }
  .tagline {
    position: absolute;
    left: 90px;
    top: 318px;
    font-family: "Mulish", "Century Gothic", sans-serif;
    font-weight: 400;
    font-size: 17px;
    line-height: 1.2;
    letter-spacing: 3px;
    text-transform: uppercase;
    color: var(--ink-muted);
  }
  .contact-list {
    position: absolute;
    right: 52px;
    top: 378px;
    list-style: none;
    font-family: "Questrial", "Century Gothic", sans-serif;
    color: var(--ink-soft);
    text-align: right;
  }
  .contact-item {
    display: flex;
    justify-content: flex-end;
    align-items: center;
    gap: 16px;
    height: 44px;
    font-size: 22px;
    white-space: nowrap;
  }
  .contact-item .icon-slot {
    width: 24px;
    display: flex;
    justify-content: center;
  }
  .contact-item.web {
    font-size: 24px;
    letter-spacing: 2.5px;
  }
  .contact-icon {
    width: 20px;
    height: 20px;
    fill: none;
    stroke: var(--ink-soft);
    stroke-width: 1.8;
    stroke-linejoin: round;
  }
</style>
</head>
<body>
  <main class="canvas">
    <section class="business-card" aria-label="Ledgerwise Partners business card">
      <div class="accent-band"></div>

      <div class="brand">
        <span class="brand-mark"></span>
        <h1 class="brand-name">
          <span class="line">Ledgerwise</span>
          <span class="line line-indented">Partners</span>
        </h1>
      </div>

      <p class="holder">
        <span class="holder-name">Dana Marlow</span><span class="holder-divider">|</span><span class="holder-role">Ceo</span>
      </p>

      <p class="tagline">Accelerating Cashflow</p>

      <ul class="contact-list">
        <li class="contact-item phone">
          <span>(555) 014-2290</span>
          <span class="icon-slot">
            <svg class="contact-icon" viewBox="0 0 20 20" aria-hidden="true">
              <path d="M3 8 C3 5 6 4 10 4 C14 4 17 5 17 8 L14 9 L13 7 C11 6.5 9 6.5 7 7 L6 9 Z"/>
              <rect x="6" y="10" width="8" height="6" rx="1"/>
            </svg>
          </span>
        </li>
        <li class="contact-item email">
          <span>dana@ledgerwisepartners.com</span>
          <span class="icon-slot">
            <svg class="contact-icon" viewBox="0 0 20 20" aria-hidden="true">
              <rect x="2.5" y="5" width="15" height="10" rx="1"/>
              <path d="M2.5 5.5 L10 11 L17.5 5.5"/>
            </svg>
          </span>
        </li>
        <li class="contact-item web">
          <span>www.ledgerwise.com</span>
          <span class="icon-slot"></span>
        </li>
      </ul>
    </section>
  </main>
</body>
</html>
```